Founder / concept developer needs business card // Consultant needs VCARD

I need a business card for me as a founding consultant in Berlin. I advise entrepreneurs, especially in the design of business ideas, business plans or financing applications. More information about this in the annexes. My USP: I design / structure complex ideas and projects convincingly so that my client is successful. I want to communicate professionalism, effectiveness and clarity. Colors like from the range BLACK-GRAY-GREEN. I am 27 years old, I have studied business for 7 years. Attachments: - Business card design (only idea, do not focus on it) - Website screenshot (only idea, do not focus on it)

Target Market(s)

Target group: Founder (20-50 yrs, m / w, needy, in "break-up phase") and CONTRACTOR / "financier" (30-55 yrs, m / w, often public service "routine-oriented"). The foundations are in quite different industries: digital, craft, tourism, retail, services, etc. Almost all German.

Industry/Entity Type

Consultant

Contact Information for Business Card

Lukas Brandvik
M. Sc., International Business Administration
Gründungsberater, Konzeptentwickler
www.falkenhorn-beratung.de
kontakt@falkenhorn-beratung.de
Tel. 0471 239 5518

Colors

Designer to choose colors to be used in the design.

Requirements
Must have
• Professionalism, persuasiveness, clarity
Nice to have
• memorability
Should not have
• Schnörkelei

```html
<!DOCTYPE html>
<html lang="de">
<head>
<meta charset="utf-8">
<title>Falkenhorn Beratung – Visitenkarte</title>
<link rel="stylesheet" href="https://fonts.googleapis.com/css2?family=Montserrat:wght@400;600;700;800&display=swap">
<style>
  :root {
    --page-bg: #e6e6e4;
    --card-black: #1f1f21;
    --card-shade: #18181a;
    --brand-green: #35b34a;
    --band-gray: #4a4a4c;
    --band-light: #7a7a7c;
    --text-white: #ffffff;
    --text-soft: #d8d8d8;
  }
  * { margin: 0; padding: 0; box-sizing: border-box; }
  html, body { width: 1200px; height: 913px; overflow: hidden; }
  body {
    background: var(--page-bg);
    font-family: "Montserrat", Arial, sans-serif;
    display: flex; flex-direction: column; align-items: center; justify-content: center;
    gap: 44px;
  }
  .card {
    position: relative; width: 640px; height: 376px;
    background: var(--card-black); overflow: hidden;
    box-shadow: 0 8px 22px rgba(0,0,0,.25);
  }
  .card-art { position: absolute; inset: 0; width: 100%; height: 100%; }
  .wordmark {
    position: absolute; color: var(--brand-green); font-weight: 800;
    text-transform: uppercase; line-height: .95; display: flex; align-items: center;
  }
  .wordmark-square { background: var(--brand-green); flex: none; }
  .front .wordmark { left: 150px; top: 134px; font-size: 44px; letter-spacing: 3px; gap: 18px; }
  .front .wordmark-square { width: 56px; height: 56px; }
  .back .wordmark { left: 34px; top: 250px; font-size: 24px; letter-spacing: 2px; gap: 10px; }
  .back .wordmark-square { width: 30px; height: 30px; }

  .contact { position: absolute; left: 300px; top: 40px; color: var(--text-white); }
  .contact-name {
    color: var(--brand-green); font-weight: 800; font-size: 25px;
    letter-spacing: 1px; text-transform: uppercase; margin-bottom: 8px;
  }
  .contact-degree { font-size: 10.5px; color: var(--text-soft); line-height: 1.3; }
  .contact-role { font-size: 14px; font-weight: 700; line-height: 1.25; margin-top: 4px; margin-bottom: 14px; }
  .contact-list { list-style: none; }
  .contact-item { display: flex; align-items: center; gap: 12px; height: 32px; font-size: 13px; }
  .contact-item.plain { padding-left: 54px; }
  .icon-tag { width: 42px; height: 26px; flex: none; }
  .accent-line { position: absolute; left: 282px; top: 46px; width: 2px; height: 26px; background: var(--brand-green); }
</style>
</head>
<body>

<section class="card front" aria-label="Visitenkarte Vorderseite">
  <svg class="card-art" viewBox="0 0 640 376" aria-hidden="true">
    <polygon points="120,0 330,0 190,376 0,376 0,300" fill="var(--card-shade)"/>
    <polygon points="470,0 640,0 640,120" fill="var(--card-shade)"/>
    <polygon points="540,196 640,160 640,214 560,240" fill="var(--band-light)"/>
    <polygon points="300,312 640,200 640,262 300,376" fill="var(--band-gray)"/>
    <polygon points="0,304 248,304 304,330 304,376 0,376" fill="var(--brand-green)"/>
  </svg>
  <div class="wordmark">
    <span class="wordmark-square"></span>
    <span>Falkenhorn<br>Beratung</span>
  </div>
</section>

<section class="card back" aria-label="Visitenkarte Rückseite">
  <svg class="card-art" viewBox="0 0 640 376" aria-hidden="true">
    <polygon points="60,120 250,120 200,376 20,376" fill="var(--card-shade)"/>
    <polygon points="530,226 640,200 640,290 540,300" fill="var(--brand-green)"/>
    <polygon points="200,326 430,270 440,290 210,348" fill="var(--band-light)"/>
    <polygon points="200,350 640,290 640,330 230,376 200,376" fill="var(--band-gray)"/>
  </svg>
  <span class="accent-line"></span>
  <div class="wordmark">
    <span class="wordmark-square"></span>
    <span>Falkenhorn<br>Beratung</span>
  </div>
  <div class="contact">
    <p class="contact-name">Lukas Brandvik</p>
    <p class="contact-degree">M. Sc., International<br>Business Administration</p>
    <p class="contact-role">Gründungsberater,<br>Konzeptentwickler</p>
    <ul class="contact-list">
      <li class="contact-item">
        <svg class="icon-tag" viewBox="0 0 42 26" aria-hidden="true">
          <polygon points="0,0 32,0 42,13 32,26 0,26" fill="var(--brand-green)"/>
          <rect x="12" y="5" width="10" height="16" rx="2" fill="none" stroke="#fff" stroke-width="2"/>
          <line x1="15" y1="17" x2="19" y2="17" stroke="#fff" stroke-width="1.5"/>
        </svg>
        <span>0471 239 5518</span>
      </li>
      <li class="contact-item">
        <svg class="icon-tag" viewBox="0 0 42 26" aria-hidden="true">
          <polygon points="0,0 32,0 42,13 32,26 0,26" fill="var(--brand-green)"/>
          <rect x="8" y="7" width="20" height="13" fill="#fff"/>
          <polyline points="8,7 18,15 28,7" fill="none" stroke="var(--brand-green)" stroke-width="1.6"/>
        </svg>
        <span>kontakt@falkenhorn-beratung.de</span>
      </li>
      <li class="contact-item">
        <svg class="icon-tag" viewBox="0 0 42 26" aria-hidden="true">
          <polygon points="0,0 32,0 42,13 32,26 0,26" fill="var(--brand-green)"/>
          <circle cx="18" cy="13" r="8" fill="none" stroke="#fff" stroke-width="1.6"/>
          <ellipse cx="18" cy="13" rx="3.5" ry="8" fill="none" stroke="#fff" stroke-width="1.2"/>
          <line x1="10" y1="13" x2="26" y2="13" stroke="#fff" stroke-width="1.2"/>
        </svg>
        <span>www.falkenhorn-beratung.de</span>
      </li>
      <li class="contact-item plain"><span>Your Address Here</span></li>
    </ul>
  </div>
</section>

</body>
</html>
```